Need designers to make a boring check list funky and fun

We are an executive rental company based in Sydney. We deal in fully furnished properties for both short and long term bookings. We have a check list for home owners to help them prepare their home for guests.
We are looking for an interesting design which makes the mundane tasks seem both fun and enjoyable.
Target Market(s)
single, couples and families where they are dual income households. Highly educated, high powered jobs with little to no time and are stressed needing a break, but also needing to pay the mortgage.
Industry/Entity Type
It Company
Colors
Designer to choose colors to be used in the design.
Requirements
Must have
- images of house rooms, clean.
- our logo on it
Nice to have
- icons for each section ie person swimming for a pool
Should not have
- just text no images

```html
<!DOCTYPE html>
<html lang="en">
<head>
<meta charset="utf-8">
<title>Kestrel Stays – Check List for Holiday Owners</title>
<link href="https://fonts.googleapis.com/css2?family=Montserrat:wght@400;500;600;700;800&family=Lato:wght@400;700&display=swap" rel="stylesheet">
<style>
:root{
  --brand:#e4234f;
  --bar:#a9abae;
  --ink:#3f3f41;
  --muted:#6d6e71;
  --paper:#ffffff;
  --backdrop:#ecebe8;
}
*{box-sizing:border-box}
html,body{margin:0;padding:0;overflow:hidden}
body{width:848px;height:1200px;background:var(--backdrop)}
.canvas{position:relative;width:848px;height:1200px;overflow:hidden;background:var(--backdrop)}

.page{position:absolute;width:376px;height:532px;background:var(--paper);overflow:hidden;box-shadow:0 2px 8px rgba(0,0,0,.12)}
.page--cover{left:28px;top:56px}
.page--two{left:444px;top:56px}
.page--three{left:28px;top:640px}
.page--four{left:444px;top:640px}

/* cover */
.cover-brand{position:absolute;left:14px;top:22px;width:178px;text-align:center}
.cover-brand .mark{display:block;width:48px;height:48px;margin:0 auto 16px;background:var(--brand);border-radius:6px}
.cover-brand .name{font:500 12px/1 "Montserrat",sans-serif;letter-spacing:3px;color:var(--muted)}
.cover-brand .rule{height:1px;background:var(--brand);margin:9px 8px}
.cover-brand .tagline{font:400 9px/1 "Montserrat",sans-serif;letter-spacing:1.5px;color:var(--muted)}
.cover-band{position:absolute;left:0;top:161px;width:376px;height:66px;background:var(--brand)}
.cover-title{position:absolute;left:0;top:175px;width:194px;text-align:center;color:#fff;font-family:"Montserrat",sans-serif}
.cover-title .big{font-weight:800;font-size:21px;line-height:1}
.cover-title .small{font-weight:700;font-size:13px;margin-top:4px}
.cover-photo{position:absolute;left:194px;top:18px;width:164px;height:194px;
  background:linear-gradient(180deg,#d9dcd8 0%,#6b6e64 45%,#4fb8cc 62%,#2f93b3 100%);
  clip-path:polygon(0 0,100% 0,100% 92%,92% 100%,0 100%)}

/* inner page header */
.masthead{position:absolute;left:18px;top:18px;width:340px;height:23px;background:var(--brand);display:flex;align-items:center;color:#fff}
.masthead .mark{width:23px;height:23px;background:#fff;border:2px solid var(--brand)}
.masthead .name{font:500 6px/1 "Montserrat",sans-serif;letter-spacing:1.5px;margin-left:10px}
.masthead .doc{margin-left:auto;margin-right:8px;text-align:right;font:700 6px/1.35 "Montserrat",sans-serif}
.masthead .doc em{font-style:italic;font-weight:600;font-size:5px}

/* sections */
.section{position:absolute;left:18px;width:340px}
.section--half{width:162px}
.bar{position:relative;height:17px;background:var(--bar);display:flex;align-items:center;padding-left:6px;
  color:#fff;font:600 12px/1 "Montserrat",sans-serif;letter-spacing:.3px}
.bar .num{color:var(--brand);font-size:8.5px;font-weight:600;margin-right:3px}
.bar .icon{position:absolute;right:0;top:-2px;width:30px;height:21px;background:#fff;border-radius:11px 3px 3px 11px;
  border-right:3px solid var(--bar);display:flex;align-items:center;justify-content:center}
.bar .icon svg{width:15px;height:15px;fill:none;stroke:var(--brand);stroke-width:2;stroke-linecap:round;stroke-linejoin:round}

.tasks{list-style:none;margin:7px 0 0;padding:0;font:400 7px/1.25 "Lato",sans-serif;color:var(--ink)}
.tasks li{position:relative;padding-left:9px;margin-bottom:3.8px}
.tasks li::before{content:"";position:absolute;left:0;top:1.8px;width:4px;height:4px;border:1px solid var(--brand)}
.tasks--narrow{width:160px}
.tasks--compact{font-size:6.6px}
.tasks--compact li{margin-bottom:3.6px}
.tasks-cols{display:flex;gap:30px}
.tasks-cols .tasks{width:150px}
.tasks .continued{padding-left:0}
.tasks .continued::before{display:none}

.photo{position:absolute}
.photo--living{left:212px;top:91px;width:146px;height:188px;background:linear-gradient(160deg,#f2f2f0 0%,#c9c9c6 55%,#8c8d89 100%)}
.photo--mills{left:290px;top:359px;width:66px;height:96px;background:radial-gradient(ellipse at 50% 50%,#8c8f93 0%,#c7c9cb 45%,#fff 75%)}
.photo--towels{left:262px;top:202px;width:114px;height:88px;background:radial-gradient(ellipse at 50% 55%,#7fc84a 0%,#9ad0e6 45%,#fff 78%)}
.photo--pool{left:194px;top:405px;width:164px;height:78px;background:linear-gradient(180deg,#4c6b3a 0%,#7a9a5a 40%,#4cc3d6 70%,#2b95b2 100%)}
.photo--home{left:194px;top:238px;width:164px;height:158px;background:linear-gradient(180deg,#6aa7df 0%,#cfe6f4 50%,#8cc04f 80%,#4f8a2c 100%)}

.more{position:absolute;width:8px;height:8px}
.more svg{width:8px;height:8px;fill:none;stroke:#b7b8ba;stroke-width:1.5}

.footer{position:absolute;left:18px;top:500px;width:340px;height:13px;background:var(--brand);color:#fff;
  display:flex;justify-content:space-between;align-items:center;padding:0 9px;font:700 7.5px/1 "Montserrat",sans-serif}
.footer span{display:flex;align-items:center;gap:3px}
.footer svg{width:7px;height:7px;fill:#fff}
</style>
</head>
<body>
<div class="canvas">

  <!-- Page 1: cover -->
  <section class="page page--cover">
    <div class="cover-brand">
      <span class="mark"></span>
      <div class="name">KESTREL STAYS</div>
      <div class="rule"></div>
      <div class="tagline">STAYS MADE SIMPLE</div>
    </div>
    <div class="cover-band"></div>
    <div class="cover-photo" role="img" aria-label="Photo of a poolside terrace with outdoor lounge and umbrellas"></div>
    <div class="cover-title">
      <div class="big">CHECK LIST</div>
      <div class="small">for Holiday Owners</div>
    </div>

    <div class="section" style="top:256px">
      <div class="bar"><span class="num">1/12</span>GENERAL
        <span class="icon"><svg viewBox="0 0 16 16"><path d="M2 8 8 2.5 14 8"/><path d="M4 7v6.5h8V7"/><path d="M7 13.5v-3h2v3"/></svg></span></div>
      <ul class="tasks">
        <li>Provide spare light bulbs and batteries for all the remotes</li>
        <li>Put felt pads under furniture to protect the floor from scratching</li>
        <li>Put coasters under any furniture with wheels</li>
        <li>Remove any personal items such as photos, and sentimental items</li>
        <li>Lock up all linen including tea towels</li>
        <li>Unplug any home phones</li>
        <li>Leave modem in an area accessible by the guests.</li>
        <li>Network name and Password to be on sticker on device</li>
        <li>Ensure Internet is unlimited and the network name and password are provided to Kestrel Stays</li>
        <li>Property to be pest sprayed for cockroaches, and ants</li>
      </ul>
    </div>

    <div class="section" style="top:436px">
      <div class="bar"><span class="num">2/12</span>STAIRS
        <span class="icon"><svg viewBox="0 0 16 16"><path d="M3 4h11M2 8h11M1 12h11"/></svg></span></div>
      <ul class="tasks">
        <li>Check the balustrade and railings are secure</li>
        <li>Repair any loose carpet</li>
      </ul>
    </div>
    <span class="more" style="left:357px;top:478px"><svg viewBox="0 0 8 8"><path d="M2 1l3 3-3 3"/></svg></span>

    <div class="footer">
      <span><svg viewBox="0 0 8 8"><path d="M1.5 0.5h1.5l0.8 2-1 .8a4 4 0 0 0 1.9 1.9l.8-1 2 .8V6.5A1 1 0 0 1 6.5 7.5 6 6 0 0 1 .5 1.5a1 1 0 0 1 1-1z"/></svg>+61 412 555 018 (during business hours)</span>
      <span><svg viewBox="0 0 8 8"><path d="M1 1h6v6H1z"/></svg>www.kestrelstays.com.au</span>
    </div>
  </section>

  <!-- Page 2 -->
  <section class="page page--two">
    <header class="masthead"><span class="mark"></span><span class="name">KESTREL STAYS</span>
      <span class="doc">Check list for Holiday Owners<br><em>Page 2/4</em></span></header>

    <div class="section" style="top:67px">
      <div class="bar"><span class="num">3/12</span>LIVING ROOM
        <span class="icon"><svg viewBox="0 0 16 16"><rect x="2" y="5" width="12" height="9" rx="2"/><path d="M5.5 1.5 8 4.5l2.5-3"/></svg></span></div>
      <ul class="tasks tasks--narrow">
        <li>Check all furniture, rugs, carpet and floors have no rips, tears, stains and are in good condition.</li>
        <li>Wash/Steam Clean cushion covers</li>
        <li>Steam clean any upholstery if it requires it</li>
        <li>If you have an animal all carpet, upholstery and rugs will need to be steam cleaned prior to guests' arrival.</li>
        <li>Put in new batteries to all remotes, smoke alarms and other such devices.</li>
        <li>Detailed instructions on how to work all electronics (in guest handbook template we provide)</li>
        <li>Pack away any faulty electrical equipment</li>
        <li>Log out of all devices and set up a guest password for StreamBox, FlixHub and cable TV accounts. (Password to go in guests manual and a sticker to go on the device)</li>
      </ul>
    </div>
    <div class="photo photo--living" role="img" aria-label="Photo of a bright, clean living room with sofa and glass coffee table"></div>

    <div class="section" style="top:313px">
      <div class="bar"><span class="num">4/12</span>KITCHEN
        <span class="icon"><svg viewBox="0 0 16 16"><path d="M4 1.5v13M2.5 1.5v4a1.5 1.5 0 0 0 3 0v-4"/><path d="M11 14.5v-13c2 1 2.5 3 2.5 5.5H11"/></svg></span></div>
      <ul class="tasks tasks--compact">
        <li>Empty Pantry (spices, salt and pepper and unopened tins can remain if you don't mind guests using them)</li>
        <li>Thoroughly clean oven and microwave.</li>
        <li>Wipe out cupboards and ensure all hinges are in working order</li>
        <li>Clean out fridge and freezer. Wipe all surfaces.</li>
        <li>Check all appliances are in working order and clean.</li>
        <li>Run Dishwasher with a dishwashing cleaner in it. Fill up the rinse aid.</li>
        <li>Remove any alcohol</li>
        <li>Remove any sentimental or expensive crockery items</li>
        <li>Check all crockery is not chipped or damaged.</li>
        <li>Leave crockery and cutlery for twice the maximum number of guests</li>
        <li>Think of getting a glass top to protect tables and cabinets especially if they are French polished.</li>
      </ul>
    </div>
    <div class="photo photo--mills" role="img" aria-label="Photo of a pair of salt and pepper mills"></div>
    <span class="more" style="left:362px;top:476px"><svg viewBox="0 0 8 8"><path d="M2 1l3 3-3 3"/></svg></span>

    <div class="footer">
      <span><svg viewBox="0 0 8 8"><path d="M1.5 0.5h1.5l0.8 2-1 .8a4 4 0 0 0 1.9 1.9l.8-1 2 .8V6.5A1 1 0 0 1 6.5 7.5 6 6 0 0 1 .5 1.5a1 1 0 0 1 1-1z"/></svg>+61 412 555 018 (during business hours)</span>
      <span><svg viewBox="0 0 8 8"><path d="M1 1h6v6H1z"/></svg>www.kestrelstays.com.au</span>
    </div>
  </section>

  <!-- Page 3 -->
  <section class="page page--three">
    <header class="masthead"><span class="mark"></span><span class="name">KESTREL STAYS</span>
      <span class="doc">Check list for Holiday Owners<br><em>Page 3/4</em></span></header>

    <div class="section" style="top:67px">
      <div class="bar"><span class="num">5/12</span>BEDROOMS
        <span class="icon"><svg viewBox="0 0 16 16"><rect x="2" y="3" width="12" height="9" rx="2"/><path d="M2 9h12M4 7h3M9 7h3M3 12v2M13 12v2"/></svg></span></div>
      <ul class="tasks">
        <li>Clear ½ the robes for the guests to use in each of the bedrooms.<br>Lock the sections you are using.</li>
        <li>Clear out draws and bedside tables</li>
        <li>Leave new mattress protectors, pillow protectors for each pillow, doona's, doona protectors, extra blankets and pillows including all sofa beds and trundle beds.</li>
      </ul>
    </div>

    <div class="section" style="top:170px">
      <div class="bar"><span class="num">6/12</span>BATHROOMS
        <span class="icon"><svg viewBox="0 0 16 16"><path d="M1.5 8h13v2a3 3 0 0 1-3 3h-7a3 3 0 0 1-3-3z"/><path d="M3.5 8V3a1.5 1.5 0 0 1 3 0M4 13l-1 1.5M12 13l1 1.5"/></svg></span></div>
      <ul class="tasks">
        <li>Treat any mouldy areas</li>
        <li>Remove any mouldy grout/silicone and have it re-grouted/resealed.</li>
        <li>If you have a shower curtain new one to be put in prior to guests</li>
        <li>Check all lights an extractor fans are working and clean</li>
        <li>Clean out all cupboards including all medicines</li>
        <li>Remove any products from the shower including body sponges</li>
        <li>Leave 1 new hair dryer</li>
      </ul>
    </div>
    <div class="photo photo--towels" role="img" aria-label="Photo of rolled fresh towels in a basket"></div>

    <div class="section" style="top:304px">
      <div class="bar"><span class="num">7/12</span>LAUNDRY
        <span class="icon"><svg viewBox="0 0 16 16"><path d="M6 4a2 2 0 1 1 2.5 2L8 7.5 1.5 12.5h13L8 7.5"/></svg></span></div>
      <ul class="tasks">
        <li>Clean out lint filter for dryer.</li>
        <li>Ensure there is a Clothes Airer (free from rust), Iron (cleaned and steam comes out clean), Ironing board with undamaged cover.</li>
        <li>Leave instructions for how to operate washing machine dryer (details to go in guest handbook template provided by Kestrel)</li>
      </ul>
    </div>

    <div class="section section--half" style="top:405px">
      <div class="bar"><span class="num">8/12</span>POOL
        <span class="icon"><svg viewBox="0 0 16 16"><path d="M1.5 10c1.5-1.5 3-1.5 4.3 0s2.8 1.5 4.3 0 3-1.5 4.4 0M1.5 13.5c1.5-1.5 3-1.5 4.3 0s2.8 1.5 4.3 0 3-1.5 4.4 0"/><circle cx="11" cy="4" r="1.6"/></svg></span></div>
      <ul class="tasks">
        <li>Check pool is compliant with the council and obtain certificate</li>
        <li>Organise regular pool cleaner</li>
        <li>Leave detailed pool instructions (in guest handbook template provided)</li>
      </ul>
    </div>
    <div class="photo photo--pool" role="img" aria-label="Photo of a garden swimming pool surrounded by tropical plants"></div>
    <span class="more" style="left:362px;top:476px"><svg viewBox="0 0 8 8"><path d="M2 1l3 3-3 3"/></svg></span>

    <div class="footer">
      <span><svg viewBox="0 0 8 8"><path d="M1.5 0.5h1.5l0.8 2-1 .8a4 4 0 0 0 1.9 1.9l.8-1 2 .8V6.5A1 1 0 0 1 6.5 7.5 6 6 0 0 1 .5 1.5a1 1 0 0 1 1-1z"/></svg>+61 412 555 018 (during business hours)</span>
      <span><svg viewBox="0 0 8 8"><path d="M1 1h6v6H1z"/></svg>www.kestrelstays.com.au</span>
    </div>
  </section>

  <!-- Page 4 -->
  <section class="page page--four">
    <header class="masthead"><span class="mark"></span><span class="name">KESTREL STAYS</span>
      <span class="doc">Check list for Holiday Owners<br><em>Page 4/4</em></span></header>

    <div class="section" style="top:60px">
      <div class="bar"><span class="num">9/12</span>OUTSIDE
        <span class="icon"><svg viewBox="0 0 16 16"><path d="M3 13C2 7 6 3 14 2c0 8-4 12-10 11z"/><path d="M3 13 10 6"/></svg></span></div>
      <div class="tasks-cols">
        <ul class="tasks">
          <li>Ensure all balconies, railings, fences and flooring are stable and safe.</li>
          <li>Check height of balcony railings are compliant</li>
          <li>Get Gardener to tidy garden, weed, remove any dead branches and mulch garden beds.</li>
          <li>Arrange gardener to maintain gardens regularly (every 2 weeks) whilst you are away</li>
          <li>Ensure automatic watering system is installed and functioning</li>
          <li>Clean BBQ, fit pits and outdoor heaters</li>
        </ul>
        <ul class="tasks">
          <li class="continued">and ensure gas bottle is full if needed and or extra wood is provided.</li>
          <li>Jet blast mouldy or mildew from all outdoor surfaces</li>
          <li>Remove cobwebs</li>
          <li>Clean out gutters</li>
          <li>Remove any stray item including pet toys.</li>
          <li>Ensure outdoor lighting is operational</li>
          <li>Ensure all pathways and stairs are safe and all gates are functioning and secure</li>
          <li>Parking, provide parking dimensions</li>
          <li>Windows to be cleaned and sparkling</li>
        </ul>
      </div>
    </div>

    <div class="section section--half" style="top:240px">
      <div class="bar"><span class="num">10/12</span>SAFETY
        <span class="icon"><svg viewBox="0 0 16 16"><path d="M1.5 8a6.5 6.5 0 0 1 13 0z"/><path d="M8 8v5a1.5 1.5 0 0 1-3 0"/></svg></span></div>
      <ul class="tasks">
        <li>Provide fire extinguisher, fire blanket and first aid kit</li>
        <li>Repair leaking taps, broken tiles, etc</li>
        <li>Patch and holes in walls</li>
        <li>Check smoke alarms functioning</li>
      </ul>
    </div>
    <div class="photo photo--home" role="img" aria-label="Illustration of an open hand holding a small green house shape under a blue sky"></div>

    <div class="section section--half" style="top:337px">
      <div class="bar"><span class="num">11/12</span>INSURANCE
        <span class="icon"><svg viewBox="0 0 16 16"><circle cx="11" cy="5" r="3"/><path d="M9 7 2.5 13.5M4.5 11.5l1.5 1.5M3 13l1 1"/></svg></span></div>
      <ul class="tasks">
        <li>Get landlord and Tenants insurance</li>
        <li>Take photos of contents and of your home</li>
        <li>Lock away any valuables</li>
      </ul>
    </div>

    <div class="section" style="top:412px">
      <div class="bar"><span class="num">12/12</span>YOU'RE ALMOST THERE... FINAL BITS
        <span class="icon"><svg viewBox="0 0 16 16"><circle cx="8" cy="8" r="6.3"/><path d="M5 8.3 7.2 10.5 11 6"/></svg></span></div>
      <ul class="tasks">
        <li>Provide 4 sets of keys for Kestrel Stays</li>
        <li>Arrange rubbish to be placed out on street when required (Kestrel can arrange this at a fee)</li>
        <li>Let Kestrel know of any areas which could be affected by heavy rain</li>
        <li>Cleaners come in to set up the property prior to guests arrival</li>
      </ul>
    </div>

    <div class="footer">
      <span><svg viewBox="0 0 8 8"><path d="M1.5 0.5h1.5l0.8 2-1 .8a4 4 0 0 0 1.9 1.9l.8-1 2 .8V6.5A1 1 0 0 1 6.5 7.5 6 6 0 0 1 .5 1.5a1 1 0 0 1 1-1z"/></svg>+61 412 555 018 (during business hours)</span>
      <span><svg viewBox="0 0 8 8"><path d="M1 1h6v6H1z"/></svg>www.kestrelstays.com.au</span>
    </div>
  </section>

</div>
</body>
</html>
```